Book Cover For Future Bestselling Entrepreneurship Book

The book is called:
Cart Levers: The Quick-Lane Method to Earn Side Income and Launch a Venture in Your Off Hours

Somewhere on the cover, I'd like to experiment with a call-out that says "Featuring 300+ Apps and Marketplaces".

Author: Dale Vantry

The theme of the book is how to add your own personal "Cart Levers" on pre-existing marketplaces to reach a wide audience of buyers quickly. As far as artwork, I was thinking of a prominent literal "buy button" on the cover:
http://imgvault.east2.cdn.plimrock-media.com/dailyharrow.com/content/assets/v3/editorial/a/b7/a9f3c2d1-48e6-11e1-bc55-002b5ddf7989/7e1923c4ab8f1.image.jpg

(doesn't have to be blue or look like that, could be an more "online" looking button.)

Take a look at some of the current bestselling business books:
https://www.quillmarto.com/Top-Sellers-Reader-Shelf-Business-Investing/tops/digital-text/267930422/ref=tp_bs_nav_rshelf_2_267715122#1

I like:
https://www.quillmarto.com/Week-Venture-Build-Before-Ready-ebook/dp/Q11PXGLC9T/ref=tp_bs_267930422_75
https://www.quillmarto.com/Craft-Calling-Tested-Finding-Made-ebook/dp/Q11RYTKD2V/ref=tp_bs_267930422_18

Main criteria is something, clean and professional that still looks good in thumbnail form. If the files are delivered in a format I can edit, that's a big bonus because I'll need to make a square version for the audiobook and front/spine/back-cover for the paperback.

Dimensions 3000x4800, 300dpi

Target Market(s)

Aspiring entrepreneurs, people who want to make or need to money outside of a traditional job.

Industry/Entity Type

Small Business

Font styles to use
Sans Serif

Requirements
Must have
• Prominent Cart Levers text and a large button graphic
Nice to have
• A callout that says "Featuring 300+ Apps and Marketplaces"

```html
<!DOCTYPE html>
<html lang="en">
<head>
<meta charset="utf-8">
<title>Cart Levers — Dale Vantry</title>
<link rel="stylesheet" href="https://fonts.googleapis.com/css2?family=Questrial&display=swap">
<style>
  :root {
    --cover-teal: #1c6478;
    --button-teal: #1e687c;
    --button-rim: #247690;
    --shadow: rgba(6, 30, 40, 0.55);
    --ink-white: #ffffff;
    --accent-yellow: #f4ee1c;
    --art-warm: #e9a24a;
    --art-cool: #6fc3c0;
    --art-violet: #a982b8;
  }
  html, body {
    margin: 0;
    padding: 0;
    width: 750px;
    height: 1200px;
    overflow: hidden;
    background: var(--cover-teal);
  }
  .cover {
    position: relative;
    width: 750px;
    height: 1200px;
    background: var(--cover-teal);
    font-family: "Questrial", "Century Gothic", sans-serif;
    color: var(--ink-white);
    text-align: center;
  }
  .callout {
    position: absolute;
    top: 40px;
    left: 0;
    width: 100%;
    margin: 0;
    font-size: 30px;
    letter-spacing: 0.5px;
    font-weight: 400;
  }
  .highlight { color: var(--accent-yellow); }
  .title {
    position: absolute;
    top: 82px;
    left: 0;
    width: 100%;
    margin: 0;
    font-size: 168px;
    line-height: 148px;
    font-weight: 400;
    letter-spacing: 2px;
  }
  .title span { display: block; }
  .subtitle {
    position: absolute;
    top: 428px;
    left: 0;
    width: 100%;
    margin: 0;
    font-size: 25px;
    line-height: 37px;
    letter-spacing: 0.6px;
    font-weight: 400;
  }
  .subtitle .line { display: block; white-space: nowrap; }
  .buy-button {
    position: absolute;
    left: 165px;
    top: 555px;
    width: 420px;
    height: 420px;
  }
  .button-art {
    position: absolute;
    left: 255px;
    top: 615px;
    width: 240px;
    height: 325px;
    border-radius: 110px 110px 40px 40px;
    background: radial-gradient(circle at 45% 35%, var(--art-warm) 0%, var(--art-violet) 45%, var(--art-cool) 80%, rgba(111,195,192,0) 100%);
    opacity: 0.85;
  }
  .author {
    position: absolute;
    top: 1068px;
    left: 0;
    width: 100%;
    margin: 0;
    font-size: 88px;
    font-weight: 400;
    letter-spacing: 3px;
  }
</style>
</head>
<body>
<main class="cover">
  <p class="callout"><span class="highlight">FEATURING</span> 300+ APPS AND MARKETPLACES</p>

  <h1 class="title"><span>CART</span><span>LEVERS</span></h1>

  <p class="subtitle">
    <span class="line">THE QUICK-LANE METHOD TO <span class="highlight">EARN SIDE INCOME</span></span>
    <span class="line">AND LAUNCH A VENTURE <span class="highlight">IN YOUR OFF HOURS</span></span>
  </p>

  <svg class="buy-button" viewBox="0 0 420 420" aria-hidden="true">
    <defs>
      <filter id="button-shadow" x="-20%" y="-20%" width="140%" height="150%">
        <feDropShadow dx="0" dy="10" stdDeviation="9" flood-color="#061e28" flood-opacity="0.55"/>
      </filter>
      <radialGradient id="button-face" cx="50%" cy="40%" r="60%">
        <stop offset="0%" stop-color="#226f85"/>
        <stop offset="100%" stop-color="#1b6175"/>
      </radialGradient>
    </defs>
    <circle cx="210" cy="205" r="200" fill="url(#button-face)" stroke="var(--button-rim)" stroke-width="3" filter="url(#button-shadow)"/>
  </svg>

  <div class="button-art" role="img" aria-label="Cluster of colourful shopping speech bubbles with price, sale and payment symbols rising from a yellow shopping cart"></div>

  <p class="author">DALE VANTRY</p>
</main>
</body>
</html>
```